Corporate Business Card

Very professional, Modern, Not to busy, include phone address email, website
(253) 555-0174, 61807 19th Street N, Kent, WA 98517, marcus@kestrelbayholding.com, brelvanindustries.com

Target Market(s)

Manufacturing

Industry/Entity Type

Aero, machining, manufacturing, Off road racing

Contact Information for Business Card

Phone, address email, website

```html
<!DOCTYPE html>
<html lang="en">
<head>
<meta charset="utf-8">
<title>Brelvan Industries – Business Card</title>
<link rel="stylesheet" href="https://fonts.googleapis.com/css2?family=Exo+2:wght@600;700&family=Roboto:wght@400&display=swap">
<style>
  :root {
    --navy: #283a6e;
    --navy-deep: #24356a;
    --red: #c0232b;
    --paper: #f1f1f1;
    --white: #f4f4f4;
    --backdrop: #2a2a2a;
  }
  html, body {
    margin: 0;
    padding: 0;
    width: 1200px;
    height: 1138px;
    overflow: hidden;
    background: var(--backdrop);
  }
  .canvas {
    position: relative;
    width: 1200px;
    height: 1138px;
  }
  .card {
    position: absolute;
    width: 620px;
    height: 375px;
    border-radius: 16px;
    overflow: hidden;
  }
  .card-front {
    left: 274px;
    top: 186px;
    background: var(--navy);
  }
  .card-back {
    left: 276px;
    top: 608px;
    background: var(--paper);
  }
  .brand-name {
    position: absolute;
    left: 0;
    width: 100%;
    text-align: center;
    font-family: "Exo 2", sans-serif;
    font-weight: 700;
    margin: 0;
    line-height: 1;
    white-space: nowrap;
  }
  .card-front .brand-name {
    top: 120px;
    font-size: 58px;
    color: var(--white);
  }
  .card-back .brand-name {
    top: 56px;
    font-size: 40px;
    color: var(--navy);
  }
  .front-url {
    position: absolute;
    left: 0;
    width: 100%;
    top: 328px;
    text-align: center;
    font-family: "Roboto", sans-serif;
    font-size: 17px;
    letter-spacing: 9.4px;
    color: var(--white);
  }
  .front-url .accent { color: var(--red); }
  .wave {
    position: absolute;
    left: 0;
    top: 0;
    width: 620px;
    height: 375px;
  }
  .holder-name {
    position: absolute;
    left: 34px;
    top: 282px;
    font-family: "Exo 2", sans-serif;
    font-weight: 700;
    font-size: 25px;
    line-height: 25px;
    color: var(--white);
    text-transform: uppercase;
    margin: 0;
  }
  .contact-list {
    position: absolute;
    right: 36px;
    top: 234px;
    margin: 0;
    padding: 0;
    list-style: none;
    font-family: "Roboto", sans-serif;
    font-size: 16.5px;
    color: var(--white);
    text-align: right;
  }
  .contact-list li {
    height: 24px;
    line-height: 24px;
    display: flex;
    justify-content: flex-end;
    align-items: center;
    gap: 10px;
  }
  .contact-list li.address { margin-top: 5px; }
  .contact-icon {
    width: 16px;
    height: 16px;
    flex: none;
  }
</style>
</head>
<body>
<div class="canvas">

  <section class="card card-front">
    <p class="brand-name">Brelvan Industries</p>
    <div class="front-url">www.brelvan<span class="accent">industries</span>.com</div>
  </section>

  <section class="card card-back">
    <p class="brand-name">Brelvan Industries</p>
    <svg class="wave" viewBox="0 0 620 375" aria-hidden="true">
      <path fill="var(--navy-deep)" d="M0 157 C150 214 300 206 420 178 S575 150 620 170 L620 375 L0 375 Z"/>
      <path fill="var(--red)" d="M0 134 C150 192 300 190 420 162 S578 134 620 150 L620 162 C578 148 500 150 420 172 C300 200 150 200 0 147 Z"/>
      <path fill="var(--red)" d="M40 150 C160 190 260 196 310 192 C240 198 150 188 40 150 Z"/>
    </svg>

    <h2 class="holder-name">Marcus<br>Holt</h2>

    <ul class="contact-list">
      <li>(253) 555-0174
        <svg class="contact-icon" viewBox="0 0 16 16" aria-hidden="true"><path fill="var(--white)" d="M2 5 C2 3 4 2 8 2 S14 3 14 5 L14 7 L11 7 L11 5.5 L5 5.5 L5 7 L2 7 Z M4 8 L12 8 L14 14 L2 14 Z"/><circle cx="8" cy="11" r="1.6" fill="var(--navy)"/></svg>
      </li>
      <li>www.brelvanindustries.com
        <svg class="contact-icon" viewBox="0 0 16 16" aria-hidden="true"><rect x="1" y="3" width="14" height="10" fill="var(--white)"/><path d="M1 3 L8 9 L15 3 M1 13 L6 8 M15 13 L10 8" stroke="var(--navy)" stroke-width="1.2" fill="none"/></svg>
      </li>
      <li>marcus@kestrelbayholding.com
        <svg class="contact-icon" viewBox="0 0 16 16" aria-hidden="true"><circle cx="8" cy="8" r="7" fill="var(--white)"/><path d="M1 8 H15 M8 1 V15 M2.5 4.5 H13.5 M2.5 11.5 H13.5" stroke="var(--navy)" stroke-width="1"/><ellipse cx="8" cy="8" rx="3.2" ry="7" fill="none" stroke="var(--navy)" stroke-width="1"/></svg>
      </li>
      <li class="address">61807 19th Street N, Kent, WA 98517</li>
    </ul>
  </section>

</div>
</body>
</html>
```